BuildLinkHub.com Full Stationery Design

Business Card will have all info on it. Letterhead will not have name, title or mobile number. Keep general feeling very clean, using colors from the logo as accents.
Name:Dale Morrisette
Title:President
Phone: 1-800-555-0142
Cell: 306-555-0179
email: dale@buildlinkhub.example
website: www.buildlinkhub.example
Address:
PO Box 872
Larkford, SK
S0J2T0

Target Market(s)

Construction Business owners

Industry/Entity Type

Business

Contact Information for Business Card

Name:Dale Morrisette
Title:President
Phone: 1-800-555-0142
Cell: 306-555-0179
Address:
PO Box 872
Larkford, SK
S0J2T0

Font styles to use
Sans Serif

Requirements
Must have
• Clean look
Should not have
• Images or cartoon type characters or tools

```html
<!DOCTYPE html>
<html lang="en">
<head>
<meta charset="utf-8">
<title>BuildLinkHub.com Stationery</title>
<link href="https://fonts.googleapis.com/css2?family=Poppins:wght@400;500;600&display=swap" rel="stylesheet">
<style>
  :root {
    --backdrop: #c2c2c2;
    --paper: #ececec;
    --paper-bright: #f4f4f4;
    --slate: #5f7285;
    --slate-light: #6f8293;
    --slate-dark: #4f6173;
    --orange: #d9732f;
    --red: #dc4c3a;
    --ink: #555d66;
  }
  * { box-sizing: border-box; margin: 0; padding: 0; }
  html, body { width: 1200px; height: 1200px; overflow: hidden; }
  body { background: var(--backdrop); font-family: "Poppins", sans-serif; position: relative; }
  .piece { position: absolute; }

  .brand { display: flex; align-items: center; gap: 6px; color: var(--ink); font-weight: 500; white-space: nowrap; line-height: 1; }
  .brand-square { width: 0.7em; height: 0.7em; background: var(--orange); flex: none; }
  .brand.on-dark { color: #dfe5ea; }

  /* Presentation folder, open */
  .folder-open { left: 120px; top: 160px; width: 604px; height: 432px; background: var(--paper-bright); }
  .folder-open .spine { position: absolute; left: 301px; top: 0; bottom: 0; width: 2px; background: #dedede; }
  .folder-open svg { position: absolute; left: 0; bottom: 0; }

  /* Presentation folder, cover */
  .folder-cover { left: 788px; top: 163px; width: 302px; height: 433px;
    background: linear-gradient(160deg, var(--slate-light), var(--slate)); }
  .folder-cover .brand { position: absolute; left: 56px; top: 94px; font-size: 21px; color: #808c97; }

  /* Letterhead */
  .letterhead { left: 123px; top: 640px; width: 288px; height: 408px; background: var(--paper); }
  .letterhead .brand { position: absolute; left: 20px; top: 28px; font-size: 10px; }
  .contact { position: absolute; font-size: 4.4px; line-height: 1.55; color: var(--ink); border-left: 1px solid #9aa3ab; padding-left: 4px; white-space: nowrap; }
  .letterhead .contact { left: 195px; top: 22px; }
  .contact .icon { color: var(--red); margin-right: 2px; }

  /* Envelope front */
  .envelope-front { left: 445px; top: 645px; width: 302px; height: 152px; background: var(--paper-bright); }
  .envelope-front .brand { position: absolute; left: 12px; top: 22px; font-size: 9px; }
  .envelope-front .return { position: absolute; left: 12px; top: 127px; font-size: 4.4px; line-height: 1.5; color: var(--ink); }

  /* Envelope back */
  .envelope-back { left: 446px; top: 837px; width: 301px; height: 152px; background: var(--paper-bright); }
  .envelope-back svg { position: absolute; left: 0; top: 0; }
  .envelope-back .flap-mark { position: absolute; left: 50%; top: 20px; transform: translateX(-50%); width: 18px; height: 18px; background: var(--orange); }

  /* Business cards */
  .card-front { left: 779px; top: 811px; width: 139px; height: 80px; background: #fff; }
  .card-front .brand { position: absolute; left: 10px; top: 37px; font-size: 4.8px; gap: 3px; }
  .card-front .contact { left: 72px; top: 18px; font-size: 3.3px; }
  .card-front .name { font-size: 4.4px; font-weight: 600; color: var(--ink); }
  .card-front .title { color: var(--red); }
  .card-back { left: 779px; top: 910px; width: 139px; height: 80px;
    background: linear-gradient(90deg, var(--slate-dark), var(--slate-light)); }
  .card-back .brand { position: absolute; left: 36px; top: 35px; font-size: 8px; gap: 3px; }
</style>
</head>
<body>

  <section class="piece folder-open" aria-label="Presentation folder, inside">
    <div class="spine"></div>
    <svg width="604" height="140" viewBox="0 0 604 140">
      <defs>
        <linearGradient id="pocketFill" x1="0" x2="1">
          <stop offset="0" stop-color="#d9732f"/>
          <stop offset="1" stop-color="#dc4c3a"/>
        </linearGradient>
      </defs>
      <path d="M0 6 H276 Q284 6 285 14 L297 140 H0 Z" fill="url(#pocketFill)"/>
      <path d="M604 6 H334 Q326 6 325 14 L308 140 H604 Z" fill="url(#pocketFill)"/>
    </svg>
  </section>

  <section class="piece folder-cover" aria-label="Presentation folder, cover">
    <div class="brand"><span class="brand-square"></span>BuildLinkHub.com</div>
  </section>

  <section class="piece letterhead" aria-label="Letterhead">
    <div class="brand"><span class="brand-square"></span>BuildLinkHub.com</div>
    <div class="contact">
      PO Box 872 Larkford,<br>S0J2T0<br>
      <span class="icon">&#9742;</span>1-800-555-0142<br>
      <span class="icon">&#9993;</span>dale@buildlinkhub.example<br>
      <span class="icon">&#9679;</span>www.buildlinkhub.example
    </div>
  </section>

  <section class="piece envelope-front" aria-label="Envelope, front">
    <div class="brand"><span class="brand-square"></span>BuildLinkHub.com</div>
    <div class="return">PO Box 872 Larkford,<br>S0J2T0</div>
  </section>

  <section class="piece envelope-back" aria-label="Envelope, back">
    <svg width="301" height="56" viewBox="0 0 301 56">
      <path d="M0 0 H301 L295 46 Q294 54 286 54 H15 Q7 54 6 46 Z" fill="#5f7285"/>
    </svg>
    <div class="flap-mark"></div>
  </section>

  <section class="piece card-front" aria-label="Business card, front">
    <div class="brand"><span class="brand-square"></span>BuildLinkHub.com</div>
    <div class="contact">
      <div class="name">Dale Morrisette</div>
      <div class="title">President</div>
      PO Box 872 Larkford,<br>S0J2T0<br>
      <span class="icon">&#9742;</span>1-800-555-0142<br>
      <span class="icon">&#9633;</span>306-555-0179<br>
      <span class="icon">&#9993;</span>dale@buildlinkhub.example<br>
      <span class="icon">&#9679;</span>www.buildlinkhub.example
    </div>
  </section>

  <section class="piece card-back" aria-label="Business card, back">
    <div class="brand on-dark"><span class="brand-square"></span>BuildLinkHub.com</div>
  </section>

</body>
</html>
```